Stationary and Business Card for dental office
Velbrook Endodontics
Stationary and Business Card for dental office  - Health
Creative Brief
Use same font as used in my logo
use any font that is easy to read. should go with font in the logo
Professional
Miren T. Osbury, D.D.S.
418 Pelloway Court, Suite #1 Corvale, CA 95412
info@velbrookendo.example
www.velbrookendo.example
Business card should have 2 logos, one brown and gold one with a tooth image....that is my main logo. The second logo( the one that says pdrcertified member) which I have uploaded as well can be in a corner or anywhere on the card. basically it is your choice where it goes on the card. It does not have to be the same size as my main business logo. This second logo only needs to be on the business cards. it can be black and white or color. I will leave that decision to you so if you think the colored logo goes with my logo colors, then use that. If not then, use the black and white one. I will prefer it in color. Under my name on business card, please write the following in smaller font Practice Limited to Endodontics LETTER HEAD: deisgn does not need to have the second logo (pdrcertifeid member logo). It should have my main business logo ( gold and brown one) with business name and all the other info like address, phone, fax web/email. ENVELOPE: only main business logo with business name and address. Please do not include phone/fax/ email or any other logos on the envelope. Thank you.

```html
<!DOCTYPE html>
<html lang="en">
<head>
<meta charset="utf-8">
<title>Velbrook Endodontics – Stationery Set</title>
<link rel="stylesheet" href="https://fonts.googleapis.com/css2?family=Poiret+One&family=Lato:wght@400;700&display=swap">
<style>
  :root{
    --frame:#c9a172;
    --stage:#d4d1d1;
    --paper:#ffffff;
    --brown:#3a2418;
    --gold:#c8a57b;
    --ink:#4a3a30;
    --mark-faint:#e6e4e2;
  }
  *{box-sizing:border-box;margin:0;padding:0}
  html,body{width:1200px;height:954px;overflow:hidden}
  body{background:var(--frame);position:relative;font-family:"Lato",sans-serif;color:var(--ink)}
  .stage{position:absolute;left:15px;top:15px;width:1170px;height:924px;background:var(--stage)}
  .piece{position:absolute;background:var(--paper);box-shadow:0 3px 8px rgba(0,0,0,.18);overflow:hidden}
  .wave{position:absolute;left:0;bottom:0;width:100%;display:block}
  .brand{position:absolute;display:flex;flex-direction:column;align-items:center;gap:4px}
  .brand-dot{border-radius:50%;background:var(--brown)}
  .brand-name{font-family:"Poiret One",sans-serif;color:var(--brown);white-space:nowrap;font-weight:400}
  .small-print{position:absolute;font-size:6px;line-height:1.45;color:var(--ink);text-align:right;white-space:nowrap}

  /* showcase logo */
  .showcase-brand{left:938px;top:46px;width:150px}
  .showcase-brand .brand-dot{width:40px;height:40px}
  .showcase-brand .brand-name{font-size:17px}

  /* letterhead */
  .letterhead{left:50px;top:109px;width:434px;height:574px}
  .letterhead .brand{left:18px;top:18px;width:84px}
  .letterhead .brand-dot{width:30px;height:30px}
  .letterhead .brand-name{font-size:10px}
  .letterhead .small-print{right:22px;top:30px}
  .letterhead .mark-area{position:absolute;left:124px;top:204px;width:182px;height:182px;border-radius:50%;background:radial-gradient(circle,#f1efed 0%,var(--mark-faint) 100%)}

  /* folder */
  .folder{left:536px;top:132px;width:238px;height:318px}
  .folder .slot{position:absolute;right:-34px;top:50px;width:70px;height:100px;border-radius:50%;background:var(--stage);box-shadow:inset 2px 0 3px rgba(0,0,0,.12)}
  .folder .brand{left:19px;top:112px;width:200px}
  .folder .brand-dot{width:40px;height:40px}
  .folder .brand-name{font-size:15px}

  /* disc */
  .disc{position:absolute;left:854px;top:198px;width:248px;height:248px;filter:drop-shadow(0 4px 6px rgba(0,0,0,.2))}
  .disc .brand{left:74px;top:40px;width:100px}
  .disc .brand-dot{width:30px;height:30px}
  .disc .brand-name{font-size:11px}

  /* envelope */
  .envelope{left:598px;top:598px;width:564px;height:279px}
  .envelope .flap{position:absolute;left:0;top:0;width:100%;height:42px;display:block}
  .envelope .brand{left:193px;top:130px;width:120px}
  .envelope .brand-dot{width:38px;height:38px}
  .envelope .brand-name{font-size:14px}
  .envelope .small-print{right:30px;top:148px}

  /* business cards */
  .card{width:212px;height:128px;top:756px}
  .card-front{left:63px}
  .card-back{left:329px}
  .card-front .brand{left:94px;top:12px;width:24px}
  .card-front .brand-dot{width:22px;height:22px}
  .card-front .holder{position:absolute;left:10px;top:46px;font-size:6.5px;line-height:1.4;color:var(--brown);white-space:nowrap}
  .card-front .holder strong{display:block;font-weight:700}
  .card-front .small-print{right:10px;top:42px;font-size:5.5px}
  .card-back .brand{left:43px;top:36px;width:126px}
  .card-back .brand-dot{width:26px;height:26px}
  .card-back .brand-name{font-size:11px}
  .card-back .web{position:absolute;left:0;right:0;top:94px;text-align:center;font-size:5.5px;color:var(--ink)}
</style>
</head>
<body>
<main class="stage">

  <div class="brand showcase-brand">
    <span class="brand-dot"></span>
    <span class="brand-name">Velbrook Endodontics</span>
  </div>

  <section class="piece letterhead" aria-label="Letterhead">
    <div class="brand">
      <span class="brand-dot"></span>
      <span class="brand-name">Velbrook Endodontics</span>
    </div>
    <p class="small-print">418 Pelloway Court, Suite #1<br>Corvale, CA 95412</p>
    <div class="mark-area" role="img" aria-label="Faint tooth emblem decoration"></div>
    <svg class="wave" viewBox="0 0 434 62" height="62" preserveAspectRatio="none">
      <path d="M0,30 C120,10 250,46 434,18 L434,62 L0,62Z" fill="var(--gold)"/>
      <path d="M0,26 C120,6 250,42 434,14" fill="none" stroke="var(--brown)" stroke-width="3"/>
    </svg>
  </section>

  <section class="piece folder" aria-label="Presentation folder">
    <span class="slot"></span>
    <div class="brand">
      <span class="brand-dot"></span>
      <span class="brand-name">Velbrook Endodontics</span>
    </div>
    <svg class="wave" viewBox="0 0 238 46" height="46" preserveAspectRatio="none">
      <path d="M0,24 C70,8 150,36 238,12 L238,46 L0,46Z" fill="var(--gold)"/>
      <path d="M0,20 C70,4 150,32 238,8" fill="none" stroke="var(--brown)" stroke-width="2.5"/>
    </svg>
  </section>

  <section class="disc" aria-label="Disc label">
    <svg viewBox="0 0 248 248" width="248" height="248">
      <defs><clipPath id="disc-clip"><circle cx="124" cy="124" r="124"/></clipPath></defs>
      <g clip-path="url(#disc-clip)">
        <rect width="248" height="248" fill="var(--paper)"/>
        <path d="M0,128 C70,108 170,148 248,118 L248,248 L0,248Z" fill="var(--gold)"/>
        <path d="M0,124 C70,104 170,144 248,114" fill="none" stroke="var(--brown)" stroke-width="3"/>
      </g>
      <circle cx="124" cy="124" r="20" fill="var(--stage)" stroke="#bdb8b4" stroke-width="1"/>
    </svg>
    <div class="brand">
      <span class="brand-dot"></span>
      <span class="brand-name">Velbrook Endodontics</span>
    </div>
  </section>

  <section class="piece envelope" aria-label="Envelope">
    <svg class="flap" viewBox="0 0 564 42" preserveAspectRatio="none">
      <path d="M0,0 H564 L538,42 H26Z" fill="var(--gold)"/>
    </svg>
    <div class="brand">
      <span class="brand-dot"></span>
      <span class="brand-name">Velbrook Endodontics</span>
    </div>
    <p class="small-print">418 Pelloway Court, Suite #1<br>Corvale, CA 95412</p>
    <svg class="wave" viewBox="0 0 564 46" height="46" preserveAspectRatio="none">
      <path d="M0,26 C160,8 360,40 564,14 L564,46 L0,46Z" fill="var(--gold)"/>
      <path d="M0,22 C160,4 360,36 564,10" fill="none" stroke="var(--brown)" stroke-width="3"/>
    </svg>
  </section>

  <section class="piece card card-front" aria-label="Business card front">
    <div class="brand"><span class="brand-dot"></span></div>
    <p class="holder"><strong>Miren T. Osbury, D.D.S.</strong>Practice Limited to Endodontics</p>
    <p class="small-print">418 Pelloway Court, Suite #1<br>Corvale, CA 95412<br>info@velbrookendo.example<br>www.velbrookendo.example</p>
    <svg class="wave" viewBox="0 0 212 22" height="22" preserveAspectRatio="none">
      <path d="M0,12 C60,4 130,18 212,6 L212,22 L0,22Z" fill="var(--gold)"/>
      <path d="M0,10 C60,2 130,16 212,4" fill="none" stroke="var(--brown)" stroke-width="1.5"/>
    </svg>
  </section>

  <section class="piece card card-back" aria-label="Business card back">
    <div class="brand">
      <span class="brand-dot"></span>
      <span class="brand-name">Velbrook Endodontics</span>
    </div>
    <p class="web">www.velbrookendo.example</p>
    <svg class="wave" viewBox="0 0 212 22" height="22" preserveAspectRatio="none">
      <path d="M0,12 C60,4 130,18 212,6 L212,22 L0,22Z" fill="var(--gold)"/>
      <path d="M0,10 C60,2 130,16 212,4" fill="none" stroke="var(--brown)" stroke-width="1.5"/>
    </svg>
  </section>

</main>
</body>
</html>
```